Doctors clinic requires stationary designed

We require various types of stationary to be design based on the logo (attached). We require the following:
- Letterhead (A4 Portrait)
- Business Card (must include UV spot on rear)
- With compliments slip (DL Landscape)
- Appointments card (Folded A6)

We are a young clinical practice which boasts a modern and sophisticated approach to medicine so we require something which feels fresh and modern. Please include colours represented in the logo (contrasting teal and grey). We are calling for creative minds to put forth their ideas and we will be actively providing feedback on all designs.

thank you

Clinic

```html
<!DOCTYPE html>
<html lang="en">
<head>
<meta charset="utf-8">
<title>Dr Clara Wendell – Letterhead</title>
<link href="https://fonts.googleapis.com/css2?family=Source+Sans+3:wght@400;600&display=swap" rel="stylesheet">
<style>
  :root {
    --backdrop: #cfe0df;
    --paper: #f4f5f5;
    --teal: #17877d;
    --ink: #5a5d5e;
    --ink-soft: #6c7071;
    --signature-tint: #e3e7e7;
  }
  * { box-sizing: border-box; margin: 0; padding: 0; }
  html, body {
    width: 1027px;
    height: 1200px;
    overflow: hidden;
    background: var(--backdrop);
    font-family: "Source Sans 3", "Helvetica Neue", Arial, sans-serif;
  }
  .letterhead {
    position: absolute;
    left: 103px;
    top: 20px;
    width: 820px;
    height: 1160px;
    background: var(--paper);
    color: var(--ink);
  }
  .masthead {
    position: absolute;
    top: 110px;
    left: 0;
    width: 100%;
    display: flex;
    justify-content: center;
    align-items: center;
    gap: 12px;
  }
  .masthead-dot {
    width: 22px;
    height: 22px;
    border-radius: 50%;
    background: var(--teal);
  }
  .masthead-name {
    color: var(--teal);
    font-size: 30px;
    font-weight: 400;
    letter-spacing: 0.5px;
  }
  .letter-body {
    position: absolute;
    left: 134px;
    top: 296px;
    width: 575px;
    font-size: 14.2px;
    line-height: 18px;
    color: var(--ink);
  }
  .letter-body p { margin-bottom: 18px; }
  .signature {
    position: absolute;
    left: 134px;
    top: 668px;
    width: 130px;
    height: 62px;
    background: var(--signature-tint);
    border-radius: 4px;
  }
  .sign-off {
    position: absolute;
    left: 134px;
    top: 748px;
    font-size: 14.2px;
    line-height: 17px;
    color: var(--ink);
  }
  .sign-off .role { font-size: 13px; color: var(--ink-soft); }
  .footer {
    position: absolute;
    left: 81px;
    top: 1040px;
    width: 680px;
    font-size: 10.5px;
    line-height: 16px;
    color: var(--teal);
  }
  .footer-brand {
    position: absolute;
    left: 0;
    top: 2px;
    display: flex;
    align-items: center;
    gap: 8px;
  }
  .footer-dot {
    width: 30px;
    height: 30px;
    border-radius: 50%;
    background: var(--teal);
  }
  .footer-brand-name {
    font-size: 14px;
    line-height: 15px;
    font-weight: 600;
    color: var(--teal);
  }
  .footer-brand-name span { display: block; font-size: 9.5px; line-height: 12px; }
  .footer-contact { position: absolute; left: 269px; top: 0; }
  .footer-address { position: absolute; left: 521px; top: 0; }
</style>
</head>
<body>
  <main class="letterhead">
    <header class="masthead">
      <span class="masthead-dot"></span>
      <span class="masthead-name">Dr Clara Wendell</span>
    </header>

    <section class="letter-body">
      <p>Lorem ipsum dolor sit amet,</p>
      <p>Consectetur adipiscing elit. Duis non fermentum dui. Phasellus erat tortor, faucibus vitae dui nec, lobortis aliquet purus. Integer lacinia nibh nec mi dignissim varius. In vulputate condimentum turpis, non volutpat erat condimentum posuere. In nec lorem ac felis ornare posuere. Donec non justo vulputate, laoreet justo ac, viverra turpis. Vivamus vitae sapien eget dui pellentesque pulvinar.</p>
      <p>Nullam ultrices fringilla nisi. Proin vel ipsum rhoncus, vehicula erat nec, viverra mi. Maecenas convallis turpis ac elit ornare, nec eleifend dui vehicula. Etiam rutrum dui ipsum, ac dignissim est pretium nec. Nullam venenatis lacus eget neque tempus maximus. Fusce porttitor tellus eu efficitur scelerisque. Class aptent taciti sociosqu ad litora torquent per conubia nostra, per inceptos himenaeos.</p>
      <p>Sed ornare sodales enim, ac viverra arcu sodales eget. Sed commodo nunc at tincidunt laoreet. Mauris pellentesque ex nulla, eu mollis neque sodales nec. Suspendisse potenti.</p>
      <p>Duis eu libero a massa,</p>
    </section>

    <div class="signature" role="img" aria-label="Handwritten signature of the doctor"></div>

    <div class="sign-off">
      <div class="name">Dr. Clara Wendell</div>
      <div class="role">Obstetrician and Gynaecologist</div>
    </div>

    <footer class="footer">
      <div class="footer-brand">
        <span class="footer-dot"></span>
        <div class="footer-brand-name">Dr Clara Wendell<span>Obstetrician and Gynaecologist</span></div>
      </div>
      <div class="footer-contact">
        800-555-0178<br>
        info@drclarawendell.com<br>
        www.drclarawendell.com
      </div>
      <div class="footer-address">
        48 Harbour Lane,<br>
        Lakeview State, 24680<br>
        Country
      </div>
    </footer>
  </main>
</body>
</html>
```